Tarvick homes and renovations business card design.

Would like some new card designs utilizing my new logo that look professional. I am open to different colors on the logo or utilize the same ones we have. I like the original concept but would like to see some fresh ideas and build on what we have already done.

Target Market(s)

Custom home building industry, Real estate sales, Renovation projects.

Industry/Entity Type

Home Builder

Contact Information for Business Card

Tarvick Homes and Renovations
2871 92nd Avenue
Halden Falls, Norwood
R3J2W5
Home : 403- 718-4305 Cell: 403- 294-1537

My info is : Dax Tarvick, President and CEO
email: tarvickhomes@quillpost.net
Website: tarvickhomes.net

Requirements
Must have
• Must Use my new logo design. I am open to different colors on the logo or utilize the same ones in the existing design. I can upload the original logo design if needed.

```html
<!DOCTYPE html>
<html lang="en">
<head>
<meta charset="utf-8">
<title>Tarvick Homes and Renovations – Business Card</title>
<link rel="stylesheet" href="https://fonts.googleapis.com/css2?family=Montserrat:wght@400;500;600&display=swap">
<style>
  :root {
    --backdrop: #3a3a3a;
    --card: #0b0b0b;
    --gold: #c9962e;
    --gold-bright: #e0a92a;
    --text-grey: #c9c9c9;
  }
  * { box-sizing: border-box; margin: 0; padding: 0; }
  html, body { width: 1200px; height: 864px; overflow: hidden; }
  body {
    background: var(--backdrop);
    font-family: "Montserrat", sans-serif;
    position: relative;
  }
  .card {
    position: absolute;
    width: 600px;
    height: 343px;
    background: var(--card);
    border-radius: 18px;
    box-shadow: 0 10px 28px rgba(0,0,0,0.45);
  }
  .card-front { left: 120px; top: 60px; }
  .card-back { left: 480px; top: 461px; }

  .brand {
    position: absolute;
    display: flex;
    align-items: center;
    gap: 14px;
    color: var(--gold);
    font-weight: 600;
  }
  .brand-mark {
    width: 18px; height: 18px;
    background: var(--gold-bright);
    flex: none;
  }
  .brand-name { line-height: 1.05; }
  .brand-name .line-main { display: block; font-size: 52px; letter-spacing: 1px; }
  .brand-name .line-sub { display: block; font-size: 14px; letter-spacing: 1.6px; margin-top: 4px; }

  .card-front .brand { left: 50%; top: 50%; transform: translate(-50%, -50%); }

  .card-back .brand { left: 40px; top: 150px; }
  .card-back .brand-name .line-main { font-size: 40px; }
  .card-back .brand-name .line-sub { font-size: 11px; letter-spacing: 1.2px; }

  .divider {
    position: absolute;
    left: 325px; top: 48px;
    width: 1.5px; height: 246px;
    background: var(--gold);
  }
  .contact {
    position: absolute;
    left: 348px; top: 52px;
    color: var(--text-grey);
    font-size: 13px;
    line-height: 1.4;
  }
  .contact .person { color: var(--gold); font-size: 19px; font-weight: 600; }
  .contact .title { margin-bottom: 16px; }
  .contact .address { margin-bottom: 16px; }
  .contact ul { list-style: none; }
  .contact li { display: flex; align-items: center; gap: 9px; }
  .contact svg { width: 13px; height: 13px; flex: none; }
</style>
</head>
<body>
  <section class="card card-front">
    <div class="brand">
      <span class="brand-mark"></span>
      <span class="brand-name">
        <span class="line-main">TARVICK</span>
        <span class="line-sub">HOMES AND RENOVATIONS</span>
      </span>
    </div>
  </section>

  <section class="card card-back">
    <div class="brand">
      <span class="brand-mark"></span>
      <span class="brand-name">
        <span class="line-main">TARVICK</span>
        <span class="line-sub">HOMES AND RENOVATIONS</span>
      </span>
    </div>
    <div class="divider"></div>
    <div class="contact">
      <p class="person">Dax Tarvick</p>
      <p class="title">President and CEO</p>
      <p class="address">2871 92nd Avenue<br>Halden Falls, Norwood, R3J2W5</p>
      <ul>
        <li>
          <svg viewBox="0 0 16 16" aria-hidden="true"><path fill="#e0a92a" d="M3.5 1.5l2.5 0 1 3.5-1.8 1.2c.8 1.8 2.2 3.2 4 4l1.2-1.8 3.5 1v2.5c0 .8-.7 1.5-1.5 1.5C6.5 13.4 2.6 9.5 2 3c0-.8.7-1.5 1.5-1.5z"/></svg>
          <span>403- 718-4305</span>
        </li>
        <li>
          <svg viewBox="0 0 16 16" aria-hidden="true"><rect x="4" y="1" width="8" height="14" rx="1.5" fill="none" stroke="#e0a92a" stroke-width="1.6"/><circle cx="8" cy="12.3" r="0.9" fill="#e0a92a"/></svg>
          <span>403- 294-1537</span>
        </li>
        <li>
          <svg viewBox="0 0 16 16" aria-hidden="true"><rect x="1" y="3" width="14" height="10" fill="#e0a92a"/><path d="M1 3l7 6 7-6" fill="none" stroke="#0b0b0b" stroke-width="1.3"/></svg>
          <span>tarvickhomes@quillpost.net</span>
        </li>
        <li>
          <svg viewBox="0 0 16 16" aria-hidden="true"><g fill="none" stroke="#e0a92a" stroke-width="1.3"><circle cx="8" cy="8" r="6.5"/><ellipse cx="8" cy="8" rx="3" ry="6.5"/><path d="M1.5 8h13M2.5 4.8h11M2.5 11.2h11"/></g></svg>
          <span>tarvickhomes.net</span>
        </li>
      </ul>
    </div>
  </section>
</body>
</html>
```